New template needed for Joomla 3.2 website

We are a mortgage origination company based in Johannesburg, South Africa and require a sleek, modern & professional look for our website.
The website is complete and your template should accommodate all pages on the site (there are not many) and be ready for Joomla implementation.
Our website can be viewed at www.keystonelending.example.co.za
Target Market(s)
We are targeting consumers who require mortgage finance to buy real estate. There is no particular demographic, except that we cater to South African home buyers exclusively!
Requirements
Must have
- It must look professional and modern.
Take a look at competitor websites:
www.vundo.example.co.za
www.zqbondhub.example.com
http://www.brightpathfold.example.co.za/loanpeak/
http://www.tideloan.example.co.za/
We want to beat the competition !!
Nice to have
- Website should blend with company logo and play on the symbol in the logo.
I want more of a people / photo element to the template. It needs to make us seem "tangible"

```html
<!DOCTYPE html>
<html lang="en">
<head>
<meta charset="utf-8">
<title>Keystone Lending – Home</title>
<link href="https://fonts.googleapis.com/css2?family=Open+Sans:wght@400;600;700&display=swap" rel="stylesheet">
<style>
:root{
  --brand:#0a86c4;
  --brand-dark:#0569a3;
  --brand-deep:#04578c;
  --nav-pill:#0b5f98;
  --ink:#222;
  --body:#444;
  --heading:#0c86c2;
  --soft-bg:#f3f4f5;
  --quote-bg:#eceef2;
  --white:#fff;
}
*{margin:0;padding:0;box-sizing:border-box}
html,body{width:831px;height:1200px;overflow:hidden;background:var(--white)}
body{font-family:"Open Sans",Arial,sans-serif;color:var(--ink);position:relative}
.page{position:relative;width:831px;height:1200px;overflow:hidden}

/* header */
.site-header{position:absolute;left:0;top:0;width:831px;height:70px;background:linear-gradient(#fff,#f2f4f6);border-top:5px solid var(--brand)}
.call-tab{position:absolute;right:46px;top:-5px;height:30px;width:176px;background:var(--brand);border-radius:0 0 22px 22px;color:var(--white);font-size:14px;font-weight:600;text-align:center;line-height:28px}
.brand{position:absolute;left:25px;top:24px;display:flex;align-items:center;gap:8px}
.brand-dot{width:28px;height:28px;border-radius:50%;background:var(--brand)}
.brand-name{font-size:20px;font-weight:700;color:var(--brand-deep);letter-spacing:.5px}
.main-nav{position:absolute;left:281px;top:45px;display:flex;align-items:center}
.main-nav a{font-size:13px;font-weight:600;color:var(--ink);text-decoration:none;padding:0 9px;border-left:1px solid #ddd;line-height:20px}
.main-nav a:first-child{border-left:0}
.main-nav a.active{background:var(--nav-pill);color:var(--white);border-radius:4px;padding:0 7px;margin-right:7px}
.main-nav a.active + a{border-left:0}

/* hero */
.hero{position:absolute;left:0;top:70px;width:831px;height:371px;overflow:hidden}
.hero-photo{position:absolute;left:290px;top:0;width:541px;height:371px;background:linear-gradient(135deg,#d9d3cc 0%,#c7b8ac 35%,#b9c9d6 65%,#e6e9ec 100%)}
.hero-panel{position:absolute;left:0;top:0}
.hero-copy{position:absolute;left:54px;top:86px;width:190px;color:var(--white)}
.hero-copy h1{font-size:22px;font-weight:700;line-height:25px;letter-spacing:.3px}
.hero-copy h1 span{display:block;font-size:19px}
.hero-copy p{font-size:9.3px;line-height:11.2px;margin-top:8px}
.slider-arrows{position:absolute;left:242px;top:320px;display:flex;border:1px solid rgba(255,255,255,.6);border-radius:4px;overflow:hidden}
.slider-arrows span{width:22px;height:25px;display:flex;align-items:center;justify-content:center;background:rgba(255,255,255,.12)}
.slider-arrows span+span{border-left:1px solid rgba(255,255,255,.6)}

/* welcome */
.welcome{position:absolute;left:0;top:441px;width:831px;height:202px;background:linear-gradient(#fff,var(--soft-bg));text-align:center}
.section-dot{width:28px;height:28px;border-radius:50%;background:var(--brand);margin:18px auto 0}
.section-title{font-size:21px;font-weight:600;color:var(--heading);margin-top:5px}
.welcome p{width:651px;margin:8px auto 0;font-size:9.2px;line-height:15.5px;color:var(--body)}
.btn{display:inline-block;margin-top:11px;background:var(--brand);color:var(--white);font-size:11px;font-weight:600;width:77px;height:22px;line-height:22px;border-radius:4px;text-decoration:none}

/* features */
.features{position:absolute;left:0;top:643px;width:831px;height:262px}
.feature{position:absolute;top:40px;width:200px;text-align:center}
.feature-art{width:88px;height:84px;margin:0 auto;border-radius:6px}
.feature h2{font-size:18px;font-weight:600;color:var(--heading);margin-top:27px}
.feature p{font-size:13.5px;line-height:17px;color:var(--ink);margin-top:10px;font-weight:400}
.art-wallet{background:linear-gradient(135deg,#5fb3c6,#e2703f 55%,#c95a2e)}
.art-safe{background:linear-gradient(135deg,#d6d8da,#a9acaf)}
.art-cash{background:linear-gradient(135deg,#3fbf8c,#2a9f72 60%,#e7bb3a)}

/* testimonials */
.testimonials{position:absolute;left:0;top:905px;width:831px;height:212px;background:var(--quote-bg);text-align:center}
.testimonials .section-dot{margin-top:30px;width:30px;height:30px}
.testimonials .section-title{font-size:18px;margin-top:4px}
.testimonials blockquote{width:620px;margin:9px auto 0;font-size:10.5px;line-height:15px;color:#333;font-weight:600}
.testimonials cite{display:block;margin-top:9px;font-style:normal;font-size:10.5px;font-weight:700;color:#333}
.quote-arrow{position:absolute;top:117px}
.quote-arrow.prev{left:32px}
.quote-arrow.next{right:32px}

/* footer */
.site-footer{position:absolute;left:0;top:1117px;width:831px;height:83px;background:linear-gradient(var(--brand),var(--brand-dark));text-align:center;color:#5fb6e4;font-size:12px;font-weight:700;line-height:15px;padding-top:37px}
</style>
</head>
<body>
<div class="page">
  <header class="site-header">
    <div class="call-tab">Call: (010) 555 0142</div>
    <div class="brand"><span class="brand-dot"></span><span class="brand-name">KEYSTONE LENDING</span></div>
    <nav class="main-nav">
      <a class="active" href="#">Home</a>
      <a href="#">About</a>
      <a href="#">Information</a>
      <a href="#">Homeloan Calculators</a>
      <a href="#">Apply On-Line</a>
      <a href="#">Contact</a>
    </nav>
  </header>

  <section class="hero">
    <div class="hero-photo" role="img" aria-label="Photo of a smiling group of young people reviewing documents together at a bright office table"></div>
    <svg class="hero-panel" width="831" height="371" viewBox="0 0 831 371" aria-hidden="true">
      <defs>
        <linearGradient id="heroBlue" x1="0" y1="0" x2="1" y2="0">
          <stop offset="0" stop-color="#0a7fc0"/>
          <stop offset="1" stop-color="#0a8dcf"/>
        </linearGradient>
      </defs>
      <path d="M0 0 H368 C320 80 290 180 312 260 C322 300 340 340 368 371 H0 Z" fill="url(#heroBlue)"/>
      <path d="M368 0 C320 80 290 180 312 260 C322 300 340 340 368 371" fill="none" stroke="#5ab7e6" stroke-width="3"/>
    </svg>
    <div class="hero-copy">
      <h1>FAST HOMELOANS<span>GREAT SERVICE</span></h1>
      <p>Lorem ipsum dolor sit amet, consectetur adipiscing elit. Donec a eleifend nulla. Integer sit amet orci turpis. In elit felis, malesuada non suscipit et, consequat id nibh. Fusce congue erat mauris, sit amet eleifend ante tincidunt in. Nullam eget lectus at ipsum eleifend malesuada eget id lacus.</p>
    </div>
    <div class="slider-arrows">
      <span><svg width="8" height="12" viewBox="0 0 8 12"><path d="M6 1 1 6l5 5" fill="none" stroke="#fff" stroke-width="1.6"/></svg></span>
      <span><svg width="8" height="12" viewBox="0 0 8 12"><path d="M2 1l5 5-5 5" fill="none" stroke="#fff" stroke-width="1.6"/></svg></span>
    </div>
  </section>

  <section class="welcome">
    <div class="section-dot"></div>
    <h2 class="section-title">Welcome to Keystone Lending</h2>
    <p>Lorem ipsum dolor sit amet, consectetur adipiscing elit. Donec a eleifend nulla. Integer sit amet orci turpis. In elit felis, malesuada non suscipit et, consequat id nibh. Fusce congue erat mauris, sit amet eleifend ante tincidunt in. Nullam eget lectus at ipsum eleifend malesuada eget id lacus. Morbi metus lectus, porta a eros sed, pretium pretium tellus. Etiam nec mauris urna. Nulla pellentesque odio quis mauris facilisis ullamcorper. Curabitur semper augue vel fermentum semper. Praesent eu velit blandit, semper dolor et, sagittis massa.</p>
    <a class="btn" href="#">Read More</a>
  </section>

  <section class="features">
    <div class="feature" style="left:78px">
      <div class="feature-art art-wallet" role="img" aria-label="Illustration of an orange wallet holding a bank card"></div>
      <h2>100% Free of Charge</h2>
      <p>No hidden costs or service charges. Our fee is not hidden within the finance charges of your homeloan.</p>
    </div>
    <div class="feature" style="left:308px">
      <div class="feature-art art-safe" role="img" aria-label="Illustration of a grey steel safe"></div>
      <h2>Exceptional Service</h2>
      <p>No hidden costs or service charges. Our fee is not hidden within the finance charges of your homeloan.</p>
    </div>
    <div class="feature" style="left:551px">
      <div class="feature-art art-cash" role="img" aria-label="Illustration of green banknotes and a stack of gold coins"></div>
      <h2>Credit Help</h2>
      <p>No hidden costs or service charges. Our fee is not hidden within the finance charges of your homeloan.</p>
    </div>
  </section>

  <section class="testimonials">
    <div class="section-dot"></div>
    <h2 class="section-title">What Our Customers Say</h2>
    <blockquote>“Donec odio nisl, auctor eu leo adipiscing, luctus elementum ligula. Donec sed commodo turpis. Nam eleifend, risus vel tempor egestas, sem felis vulputate urna, at egestas lorem felis non nunc. Donec mattis ultrices tempus. Pellentesque habitant morbi tristique senectus et netus et malesuada fames ac turpis egestas.”</blockquote>
    <cite>– Curabitur Egestsaemper Valaugue</cite>
    <svg class="quote-arrow prev" width="14" height="26" viewBox="0 0 14 26" aria-hidden="true"><path d="M13 1 1 13l12 12" fill="none" stroke="#2e5f99" stroke-width="1.5"/></svg>
    <svg class="quote-arrow next" width="14" height="26" viewBox="0 0 14 26" aria-hidden="true"><path d="M1 1l12 12L1 25" fill="none" stroke="#2e5f99" stroke-width="1.5"/></svg>
  </section>

  <footer class="site-footer">
    Built with HTML5 and CSS3<br>
    Copyright © 2014 Keystone Lending (Pty) Ltd
  </footer>
</div>
</body>
</html>
```